Bref créative
New Corporate Website - Blue Falcons
Blue Falcons - Marketing & Lead Generation
Marketing
Does not yet exist
Blue Falcons is a new Marketing and Sales Lead generation agency specializing in helping companies analyze, pursue and close sales opportunities generated via the Internet. We provide access to our exclusive Blue Falcon Striker platform for capturing and pursing sales opportunities generated via the online platform.
I'd like to showcase a lot of red on this website. This is a new website for a new company we are starting.
The website is to feature both our online web software as well as our consulting services.
High Tech
Red (#aa0000)
Grey (#cccccc)
Verdana
Century Gothic
top
http://www.vortelix.com
http://www.brinaxo.com/en
http://www.quombrel.com
The page should include links for
Navigation
- About Blue Falcons
- Services & Solutions
- Results
- News & Announcements
- Contact Us
Also, an area for current customer's to login
please incorporate the logo of the man riding the horse backwards.

```html
<!DOCTYPE html>
<html lang="en">
<head>
<meta charset="utf-8">
<title>Blue Falcons - Marketing &amp; Lead Generation</title>
<link rel="stylesheet" href="https://fonts.googleapis.com/css2?family=Oswald:wght@400;500&family=PT+Sans:wght@400;700&display=swap">
<style>
:root{
  --red:#aa0000;
  --red-bright:#d40f0f;
  --red-deep:#6e0000;
  --red-darkest:#4a0000;
  --grey:#cccccc;
  --grey-light:#eeeeee;
  --grey-dark:#555555;
  --white:#ffffff;
  --text:#333333;
}
*{box-sizing:border-box;margin:0;padding:0}
html,body{width:1200px;height:725px;overflow:hidden}
body{
  font-family:"PT Sans",Verdana,sans-serif;
  color:var(--white);
  background:radial-gradient(ellipse at 50% 30%,#b50d0d 0%,#8f0000 45%,#5a0000 100%);
  position:relative;
}
.backdrop-art{position:absolute;inset:0;
  background:radial-gradient(ellipse 260px 200px at 120px 640px,rgba(60,0,0,.55),transparent 70%),
             radial-gradient(ellipse 220px 180px at 1080px 110px,rgba(255,255,255,.06),transparent 70%);}
.page{position:absolute;left:233px;top:58px;width:737px}
.main-nav{height:32px;display:flex;justify-content:space-around;align-items:center;
  background:linear-gradient(#e01414,#a30000);border-radius:6px 6px 0 0;
  box-shadow:0 2px 4px rgba(0,0,0,.4)}
.main-nav a{color:var(--white);text-decoration:none;font-size:13px}
.hero{display:flex;height:262px;margin-top:6px}
.brand-panel{width:211px;position:relative;
  background:linear-gradient(#ffffff,#e4e4e4 70%,#c9c9c9)}
.brand-mark{position:absolute;left:16px;top:116px;display:flex;align-items:center;gap:8px}
.brand-mark .dot{width:16px;height:16px;border-radius:50%;background:var(--red)}
.brand-mark .name{font-family:"Oswald",sans-serif;font-weight:500;font-size:26px;color:var(--red);letter-spacing:.5px;white-space:nowrap}
.brochure{position:absolute;left:0;bottom:0;width:100%;height:60px;text-decoration:none;
  background:linear-gradient(#7a0000,#a10000);display:flex;align-items:center;gap:10px;padding-left:8px}
.brochure svg{flex:none}
.brochure .label{font-family:"Oswald",sans-serif;line-height:1.1;border-left:1px solid rgba(255,255,255,.4);padding-left:8px}
.brochure .label b{display:block;font-weight:400;font-size:17px;color:#ffd9d9}
.brochure .label span{font-size:13px;color:var(--white)}
.hero-photo{flex:1;position:relative;
  background:linear-gradient(160deg,#e8e8e8 0%,#c4c4c4 50%,#9a9a9a 100%)}
.tagline{position:absolute;right:0;bottom:0;width:300px;height:30px;
  background:rgba(40,40,40,.85);font-size:12px;display:flex;align-items:center;justify-content:center}
.welcome{background:linear-gradient(#9c0000,#7d0000);padding:10px 12px 12px;height:100px}
.welcome h1{font-family:"Oswald",sans-serif;font-weight:400;font-size:17px;margin-bottom:4px}
.welcome p{font-size:10.5px;line-height:1.35;color:#ffe5e5}
.boxes{display:flex;justify-content:space-between;margin-top:14px}
.box{width:230px;height:166px;background:var(--white);color:var(--text);position:relative;
  border-top:3px solid var(--grey)}
.box h2{font-family:"Oswald",sans-serif;font-weight:400;font-size:15px;color:var(--grey-dark);
  padding:7px 8px 5px;border-bottom:1px solid var(--grey-light)}
.box h2 em{font-style:normal;color:var(--red)}
.box p{font-size:10.5px;line-height:1.3;padding:6px 8px 0}
.login-form{padding:8px 10px}
.login-form input{display:block;width:150px;height:20px;margin-bottom:8px;border:1px solid var(--grey);
  font-size:10px;padding:0 6px;color:#999}
.login-btn{position:absolute;right:18px;top:112px;background:var(--red);color:var(--white);border:0;
  font-size:10px;padding:3px 12px;border-radius:3px}
.forgot{position:absolute;left:8px;bottom:8px;font-size:10px}
.forgot a,.more{color:var(--red)}
.more{position:absolute;right:8px;bottom:6px;font-size:10px}
.news-item{padding:6px 8px 0;font-size:10.5px;line-height:1.3}
.news-item .date{display:flex;align-items:center;gap:4px;font-weight:700;color:var(--text)}
.site-footer{position:absolute;left:0;right:0;top:676px;text-align:center;font-size:10px;color:#ffd0d0}
</style>
</head>
<body>
<div class="backdrop-art" role="img" aria-label="Dark red backdrop with faint horseman silhouette"></div>
<div class="page">
  <nav class="main-nav">
    <a href="#">Home</a><a href="#">Services &amp; Solutions</a><a href="#">Results</a>
    <a href="#">News &amp; Announcements</a><a href="#">Contact Us</a>
  </nav>
  <section class="hero">
    <div class="brand-panel">
      <div class="brand-mark"><span class="dot"></span><span class="name">BLUE FALCONS</span></div>
      <a class="brochure" href="#">
        <svg width="34" height="34" viewBox="0 0 34 34"><rect x="1" y="1" width="32" height="32" fill="none" stroke="#fff" stroke-opacity=".5"/><path d="M17 8v14M11 16l6 6 6-6M9 26h16" stroke="#fff" stroke-width="2" fill="none"/></svg>
        <span class="label"><b>Download</b><span>Blue Falcon Brochure</span></span>
      </a>
    </div>
    <div class="hero-photo" role="img" aria-label="Hero photograph: rows of white spheres with one red sphere standing out">
      <div class="tagline">Marketing and Sales Lead Generation Agency</div>
    </div>
  </section>
  <section class="welcome">
    <h1>Welcome to</h1>
    <p>Lorem ipsum dolor sit amet, consectetur adipisicing elit, sed do eiusmod tempor incididunt ut labore et dolore magna aliqua. Ut enim ad minim veniam, quis nostrud exercitation ullamco laboris nisi ut aliquip ex ea commodo consequat. Duis aute irure dolor in reprehenderit in voluptate velit esse cillum dolore eu fugiat nulla pariatur. Excepteur sint occaecat cupidatat non proident, sunt in culpa qui officia deserunt mollit anim id est laborum.</p>
  </section>
  <section class="boxes">
    <div class="box">
      <h2>Customer <em>Login</em></h2>
      <form class="login-form">
        <input type="text" placeholder="Username">
        <input type="password" placeholder="********">
      </form>
      <button class="login-btn" type="button">Login</button>
      <div class="forgot">Forgot Passwod? New user <a href="#">Register</a></div>
    </div>
    <div class="box">
      <h2>Services &amp; <em>Solutions</em></h2>
      <p>Lorem ipsum dolor sit amet, consectetur adipisicing elit, sed do eiusmod tempor incididunt ut labore et dolore magna aliqua. Ut enim ad minim veniam, quis nostrud exercitation ullamco laboris nisi ut aliquip ex ea commodo consequat.</p>
      <a class="more" href="#">[read more]</a>
    </div>
    <div class="box">
      <h2>News &amp; <em>Announcements</em></h2>
      <div class="news-item">
        <div class="date"><svg width="11" height="11" viewBox="0 0 11 11"><rect x=".5" y="1.5" width="10" height="9" fill="#fff" stroke="#aa0000"/><rect x=".5" y="1.5" width="10" height="3" fill="#aa0000"/></svg>10-5-2011</div>
        Lorem ipsum dolor sit amet, consectetur adipisicing elit sed do eiusmod
      </div>
      <div class="news-item">
        <div class="date"><svg width="11" height="11" viewBox="0 0 11 11"><rect x=".5" y="1.5" width="10" height="9" fill="#fff" stroke="#aa0000"/><rect x=".5" y="1.5" width="10" height="3" fill="#aa0000"/></svg>10-5-2011</div>
        Lorem ipsum dolor sit amet, consectetur adipisicing elit sed do eiusmod
      </div>
      <a class="more" href="#">[read more]</a>
    </div>
  </section>
</div>
<footer class="site-footer">Copyright © 2011, Blue Falcons. All Rights Reserved.</footer>
</body>
</html>
```